Kestrel Bridge Consulting (KBC) Business Card Design

I would like to create double-sided business cards that contain:
1) Name: Derek Molvane
2) Phone Number: +1 (555) 218-4907
3) Email: Derek.Molvane@KestrelBridgeConsulting.example
4) Website: KestrelBridgeConsulting.example

I would like to include my logo and a color scheme similar to the Varnholt Grand Prix Ostera squad color scheme (black, silver, greenish-blue – but can also include regular blue)

What we do: Our company develops and delivers innovative and pragmatic information technology and cybersecurity risk and compliance solutions for organizations in the commercial market as well as the federal, and state/local sectors.

```html
<!DOCTYPE html>
<html lang="en">
<head>
<meta charset="UTF-8">
<title>Kestrel Bridge Consulting – Business Card</title>
<link rel="stylesheet" href="https://fonts.googleapis.com/css2?family=Exo+2:wght@400;500;700&display=swap">
<style>
  :root {
    --backdrop: #7d7f83;
    --ink: #1f232b;
    --navy: #111624;
    --navy-soft: #1c2333;
    --silver-light: #f7f7f8;
    --silver-mid: #dcdde0;
    --teal: #2bb3b1;
    --blue: #1f6fb5;
    --muted: #3a3e46;
    --white: #ffffff;
  }
  * { margin: 0; padding: 0; box-sizing: border-box; }
  html, body {
    width: 1200px; height: 781px; overflow: hidden;
    background: var(--backdrop);
    font-family: "Exo 2", sans-serif;
  }
  .canvas {
    position: relative; width: 1200px; height: 781px;
    display: flex; align-items: center; justify-content: center; gap: 60px;
  }
  .card {
    position: relative; width: 500px; height: 286px;
    border-radius: 18px; overflow: hidden;
    box-shadow: 0 14px 30px rgba(0,0,0,0.35);
  }
  /* Front */
  .card-front {
    background: linear-gradient(120deg, var(--silver-light) 0%, var(--silver-mid) 45%, var(--silver-light) 70%, var(--silver-mid) 100%);
  }
  .card-front .wave { position: absolute; inset: 0; width: 100%; height: 100%; }
  .holder { position: absolute; left: 34px; top: 30px; }
  .holder-name {
    font-weight: 700; font-size: 25px; letter-spacing: 1px; line-height: 1;
    text-transform: uppercase;
  }
  .holder-name .first { color: var(--blue); }
  .holder-name .last { color: var(--teal); }
  .holder-title {
    margin-top: 4px; font-size: 13px; color: var(--muted); font-weight: 400;
  }
  .contact {
    position: absolute; left: 34px; top: 112px;
    list-style: none; font-size: 13px; color: var(--ink); line-height: 1.65;
  }
  .brand {
    position: absolute; display: flex; align-items: center; gap: 10px;
  }
  .brand-mark { width: 30px; height: 30px; border-radius: 50%; background: var(--teal); flex: none; }
  .brand-name {
    font-weight: 500; text-transform: uppercase; letter-spacing: 1.5px; line-height: 1.05;
  }
  .card-front .brand { right: 28px; top: 98px; }
  .card-front .brand-name { color: var(--ink); font-size: 15px; }
  /* Back */
  .card-back {
    background: linear-gradient(135deg, var(--navy-soft) 0%, var(--navy) 55%, var(--navy-soft) 100%);
  }
  .card-back .texture {
    position: absolute; inset: 0;
    background: radial-gradient(ellipse at 55% 45%, rgba(60,90,110,0.35) 0%, rgba(17,22,36,0) 70%);
  }
  .card-back .brand { left: 50%; top: 50%; transform: translate(-50%, -50%); }
  .card-back .brand-name { color: var(--white); font-size: 19px; }
  .card-back .brand-mark { width: 36px; height: 36px; }
</style>
</head>
<body>
<main class="canvas">
  <section class="card card-front" aria-label="Card front">
    <svg class="wave" viewBox="0 0 500 286" preserveAspectRatio="none" aria-hidden="true">
      <path d="M0,286 L0,180 C80,178 160,205 250,248 C300,270 350,282 410,286 Z" fill="var(--teal)"/>
      <path d="M0,286 L0,188 C80,186 160,212 250,254 C300,274 350,284 400,286 Z" fill="var(--white)"/>
      <path d="M0,286 L0,193 C80,191 160,217 250,259 C295,277 340,285 385,286 Z" fill="var(--blue)"/>
      <path d="M0,286 L0,199 C80,197 160,223 245,263 C290,280 330,286 365,286 Z" fill="var(--navy)"/>
    </svg>
    <div class="holder">
      <h1 class="holder-name"><span class="first">Derek</span> <span class="last">Molvane</span></h1>
      <p class="holder-title">Chief Executive Office</p>
    </div>
    <ul class="contact">
      <li>+1 (555) 218-4907</li>
      <li>Derek.Molvane@KestrelBridgeConsulting.example</li>
      <li>KestrelBridgeConsulting.example</li>
    </ul>
    <div class="brand">
      <span class="brand-mark"></span>
      <span class="brand-name">Kestrel<br>Bridge<br>Consulting</span>
    </div>
  </section>

  <section class="card card-back" aria-label="Card back">
    <div class="texture" role="img" aria-label="Subtle dark hexagon grid texture"></div>
    <div class="brand">
      <span class="brand-mark"></span>
      <span class="brand-name">Kestrel<br>Bridge<br>Consulting</span>
    </div>
  </section>
</main>
</body>
</html>
```